Webdesign für Anbieter von Erotik-Geschichten
Zielgruppe
Wir sind ein Anbieter von Erotik-Geschichten. Die Marke heisst Lunvo Erotica. Das Erlebnis für die Kunden soll hochwertig und persönlich wirken. Daher in keiner Art und Weise schmuddelig. Die Zielgruppe sind Frauen ab ca. 20-40. Die Geschichten werden frei lesbar sein, d.h. es ist kein Online-Shop sondern mehr eine Art Blog mit verschiedenen Geschichten.
Aufgabenstellung
Wichtig ist uns eine schlichtes, minimalistisches Design (vrgl. Tafelwerk) aber trotzdem hochwertig (leicht luxuriös) wirkend.

```html
<!DOCTYPE html>
<html lang="de">
<head>
<meta charset="utf-8">
<title>Lunvo Erotica – Geschichten</title>
<link href="https://fonts.googleapis.com/css2?family=Karla:wght@400;600;700&family=Libre+Baskerville:wght@400&display=swap" rel="stylesheet">
<style>
  :root{
    --topbar:#9a9591;
    --text:#3a3a3a;
    --muted:#8c8c8c;
    --tile:#cccccc;
    --accent:#d2553d;
    --quick:#c0614c;
    --border:#9c9c9c;
    --footer:#262626;
    --footer-bottom:#000000;
    --white:#ffffff;
    --sans:'Karla', Arial, sans-serif;
    --serif:'Libre Baskerville', Georgia, serif;
  }
  html,body{margin:0;padding:0;overflow:hidden;}
  body{width:1200px;height:2400px;background:var(--white);font-family:var(--sans);color:var(--text);}
  .page{position:relative;width:1200px;height:2400px;overflow:hidden;background:var(--white);}
  .abs{position:absolute;}

  /* top bar */
  .topbar{left:0;top:0;width:1200px;height:30px;background:var(--topbar);}
  .topbar .social{left:165px;top:10px;display:flex;gap:26px;}
  .topbar .social span{width:9px;height:9px;border-radius:50%;background:#e9e6e3;display:block;}
  .topbar .contact{right:140px;top:8px;font-size:9px;color:#f3f1ef;display:flex;align-items:center;gap:5px;}

  /* header */
  .brand{left:160px;top:64px;font-size:30px;font-weight:400;color:#1b1b1b;letter-spacing:1px;}
  .nav{top:70px;left:0;width:1200px;height:20px;font-size:15px;color:#2b2b2b;}
  .nav a{position:absolute;color:inherit;text-decoration:none;}
  .nav a.login{font-weight:600;}

  /* sidebar */
  .sidebar{left:97px;font-size:15px;line-height:24px;color:#444;letter-spacing:.3px;}
  .search{left:97px;top:335px;width:205px;height:24px;border:1px solid #777;font-size:15px;text-align:center;line-height:24px;color:#444;}

  /* tiles */
  .tile{top:186px;width:162px;height:133px;background:var(--tile);color:var(--white);font-size:16px;display:flex;align-items:center;justify-content:center;letter-spacing:.3px;}

  /* featured */
  .featured{left:328px;top:391px;width:745px;height:204px;border:1px solid var(--border);box-sizing:border-box;}
  .featured .cover{left:0;top:0;width:227px;height:202px;background:radial-gradient(ellipse at 50% 55%,#b8242a 0%,#6b1a1c 40%,#1f1414 80%);}
  .featured .zoom{left:198px;top:9px;width:18px;height:18px;}
  .featured .summary{left:227px;top:0;width:290px;height:202px;border-left:1px solid var(--border);border-right:1px solid var(--border);box-sizing:border-box;padding:10px 10px;}
  .summary h3{margin:0 0 22px;font-family:var(--serif);font-weight:400;font-size:16px;line-height:26px;color:#777;}
  .summary p{margin:0;font-size:14px;line-height:26px;color:#555;}
  .featured .narrator{left:517px;top:0;width:226px;padding:12px 9px;box-sizing:border-box;}
  .narrator h4{margin:0;font-size:15px;font-weight:700;color:var(--accent);}
  .narrator .author{margin-top:22px;display:flex;align-items:center;gap:22px;font-size:15px;color:#444;}
  .narrator p{margin:18px 0 0;font-size:10.5px;line-height:20px;color:#555;}

  /* story grid */
  .story{position:absolute;}
  .story .cover{width:100%;}
  .story .title{margin-top:16px;font-family:var(--serif);font-size:11px;color:var(--muted);text-align:center;white-space:nowrap;letter-spacing:-.2px;}
  .story .tag{margin-top:4px;font-size:9.5px;color:#a8a8a8;text-align:center;}
  .quick{position:absolute;left:32px;top:142px;width:142px;height:30px;background:var(--quick);color:#fff;font-size:16px;font-weight:600;display:flex;align-items:center;justify-content:center;}

  /* footer */
  .footer{left:0;top:1760px;width:1200px;height:578px;background:var(--footer);color:#e8e8e8;}
  .footer h5{position:absolute;margin:0;font-family:var(--serif);font-weight:400;font-size:17px;letter-spacing:3px;color:#f0f0f0;}
  .address{left:129px;top:95px;font-size:11.5px;line-height:19px;color:#e0e0e0;}
  .fsocial{left:129px;top:213px;display:flex;gap:10px;}
  .fsocial span{width:28px;height:28px;background:#6f6f6f;display:block;}
  .form label{position:absolute;font-size:11px;font-weight:700;color:#f0f0f0;}
  .form label i{color:var(--accent);font-style:normal;}
  .form .field{position:absolute;background:#fff;border:1px solid #bbb;box-sizing:border-box;}
  .send{left:463px;top:339px;width:81px;height:27px;background:#8c8a88;border:1px solid #d8d8d8;border-radius:5px;box-sizing:border-box;color:#fff;font-size:13px;font-weight:700;display:flex;align-items:center;justify-content:center;}
  .legal a{position:absolute;left:463px;font-size:13.5px;color:#e8e8e8;text-decoration:none;}
  .bottom{left:0;top:2338px;width:1200px;height:62px;background:var(--footer-bottom);color:#fff;font-size:16px;font-weight:600;text-align:center;line-height:19px;padding-top:10px;box-sizing:border-box;}
</style>
</head>
<body>
<div class="page">

  <div class="abs topbar">
    <div class="abs social"><span></span><span></span><span></span></div>
    <div class="abs contact">
      <svg width="7" height="10" viewBox="0 0 7 10"><rect x="0.5" y="0.5" width="6" height="9" rx="1" fill="none" stroke="#f3f1ef"/></svg>
      999 999 999 &nbsp;|&nbsp;
      <svg width="10" height="9" viewBox="0 0 10 9"><path d="M1 1h8v5H4L2 8V6H1z" fill="none" stroke="#f3f1ef"/></svg>
      noreply@example.com
    </div>
  </div>

  <div class="abs brand">Lunvo</div>
  <nav class="abs nav">
    <a style="left:616px">Home</a>
    <a style="left:696px">Geschichten</a>
    <a style="left:830px">Über uns</a>
    <a style="left:935px">Kontakt</a>
    <a class="login" style="left:1030px">Login</a>
  </nav>

  <div class="abs sidebar" style="top:211px">Filter<br>Oft gelesen<br>Länge der Geschichten<br>Bewertung</div>
  <div class="abs search">Suche</div>
  <div class="abs sidebar" style="top:372px">Kategorien<br>Arbeitsplatz<br>Ferien<br>Fesseln<br>Dreier<br>Lesbisch</div>

  <div class="abs tile" style="left:314px">Meistgelesene</div>
  <div class="abs tile" style="left:505px">Neuerscheinungen</div>
  <div class="abs tile" style="left:712px">Empfehlungen</div>
  <div class="abs tile" style="left:916px">Vorstellungen</div>

  <section class="abs featured">
    <div class="abs cover" role="img" aria-label="Titelbild: Frau im roten Kleid auf dunklem Ledersessel"></div>
    <svg class="abs zoom" viewBox="0 0 18 18"><circle cx="9" cy="9" r="9" fill="#fff"/><circle cx="8" cy="8" r="3.2" fill="none" stroke="#222" stroke-width="1.6"/><path d="M10.4 10.4l3 3" stroke="#222" stroke-width="1.8"/></svg>
    <div class="abs summary">
      <h3>Die Frau im roten Kleid - P. Morgan Inhalt</h3>
      <p>Lorem ipsum dolor sit amet , consectetuer adipiscing elit. Aenean commodo ligula eget dolor. Aenean massa. Cum sociis natoque</p>
    </div>
    <div class="abs narrator">
      <h4>Perspektive des Erzählers</h4>
      <div class="author">P. Morgan
        <svg width="48" height="48" viewBox="0 0 48 48"><circle cx="24" cy="24" r="23" fill="#fff" stroke="#333"/><circle cx="24" cy="17" r="8" fill="#000"/><path d="M9 38c2-10 9-13 15-13s13 3 15 13a23 23 0 0 1-30 0z" fill="#000"/></svg>
      </div>
      <p>Lorem ipsum dolor sit amet , consectetuer adipiscing elit. Aenean commodo ligula eget dolor. Aenean massa. Cum sociis natoque</p>
    </div>
  </section>

  <!-- row 1 -->
  <div class="story" style="left:129px;top:688px;width:207px">
    <div class="cover" style="height:243px;background:linear-gradient(90deg,#6c7178,#2a2a2c 45%,#8a8d92)" role="img" aria-label="Paar im Gegenlicht vor einem Fenster"></div>
    <div class="title">Der Butler – M.P Williams</div>
  </div>
  <div class="story" style="left:360px;top:688px;width:207px">
    <div class="cover" style="height:243px;background:linear-gradient(90deg,#b8985f,#3a3a44 50%,#c9a56a)" role="img" aria-label="Unscharfer Mann im Anzug"></div>
    <div class="title">Der Mann im Spiegel – C. Cesar</div>
  </div>
  <div class="story" style="left:590px;top:688px;width:207px">
    <div class="cover" style="height:243px;background:linear-gradient(160deg,#f3f3f5,#d9dce2 55%,#5a4036)" role="img" aria-label="Frau in weißer Bluse mit Brille im Büro"></div>
    <div class="title">Die Business Lady – R. Rocheford</div>
  </div>
  <div class="story" style="left:819px;top:688px;width:207px">
    <div class="cover" style="height:243px;background:radial-gradient(ellipse at 50% 55%,#b8242a 0%,#6b1a1c 40%,#1f1414 80%)" role="img" aria-label="Frau im roten Kleid auf dunklem Ledersessel"></div>
    <div class="quick">Kurzer Blick</div>
    <div class="title">Die Frau im roten Kleid – P. Morgan</div>
  </div>

  <!-- row 2 -->
  <div class="story" style="left:126px;top:1012px;width:208px">
    <div class="cover" style="height:245px;background:linear-gradient(90deg,#c86b8a,#4e7b84 55%,#a75a90 70%)" role="img" aria-label="Rosa Rose mit Titel Forever"></div>
    <div class="title">Forever – R. Davids</div>
    <div class="tag">Empfehlungen</div>
  </div>
  <div class="story" style="left:357px;top:1012px;width:209px">
    <div class="cover" style="height:245px;background:linear-gradient(120deg,#c9b49e,#a34a3c 50%,#d5d0c8)" role="img" aria-label="Zwei Freundinnen im Café"></div>
    <div class="title">La vie et belle – R. Rocheford</div>
    <div class="tag">Bestseller</div>
  </div>
  <div class="story" style="left:589px;top:1012px;width:208px">
    <div class="cover" style="height:245px;background:linear-gradient(135deg,#b0806a,#3b2a26 60%,#1a1414)" role="img" aria-label="Paar in inniger Umarmung"></div>
    <div class="title">Liebe auf Abwegen – T. Hawks</div>
    <div class="tag">Empfehlungen</div>
  </div>
  <div class="story" style="left:820px;top:1012px;width:208px">
    <div class="cover" style="height:245px;background:linear-gradient(180deg,#b9a793,#d2bea4 60%,#c2ad94)" role="img" aria-label="Sandstrand mit Titel Mirella"></div>
    <div class="title">Mirella – R. Michaels</div>
    <div class="tag">Bestseller, Neuerscheinungen</div>
  </div>

  <!-- row 3 -->
  <div class="story" style="left:127px;top:1350px;width:209px">
    <div class="cover" style="height:248px;background:linear-gradient(160deg,#3d8a9a,#1d4d5a 55%,#7a1c22)" role="img" aria-label="Paar unter Wasser"></div>
    <div class="title">Underwater – R. Michaels</div>
  </div>
  <div class="story" style="left:361px;top:1350px;width:209px">
    <div class="cover" style="height:248px;background:radial-gradient(ellipse at 50% 60%,#b8242a 0%,#6b1a1c 40%,#1f1414 80%)" role="img" aria-label="Frau im roten Kleid auf Ledersessel"></div>
    <div class="title">Unschuldig – P. Morgan</div>
  </div>
  <div class="story" style="left:594px;top:1350px;width:209px">
    <div class="cover" style="height:248px;background:linear-gradient(90deg,#e6e8ec,#cfd3d8 35%,#2a2426 65%,#dcdfe3)" role="img" aria-label="Frau in schwarzem Body am Fenster"></div>
    <div class="title">Verführ mich – P. Morgan</div>
  </div>
  <div class="story" style="left:827px;top:1350px;width:209px">
    <div class="cover" style="height:248px;background:linear-gradient(135deg,#b0806a,#3b2a26 60%,#1a1414)" role="img" aria-label="Paar in inniger Umarmung"></div>
    <div class="title">Verführung – T. Hawks</div>
  </div>

  <footer class="abs footer">
    <h5 style="left:129px;top:59px">Kontakt</h5>
    <div class="abs address">Lunvo Erotica<br>Musterstraße 90000<br>99999 Musterstadt<br>E-Mail: info@example.com<br>Telefonnummer: 999 999 999</div>
    <div class="abs fsocial"><span></span><span></span><span></span></div>

    <h5 style="left:463px;top:65px">Schreiben Sie uns</h5>
    <div class="form">
      <label style="left:463px;top:108px">Name <i>*</i></label>
      <div class="field" style="left:463px;top:127px;width:364px;height:25px"></div>
      <label style="left:463px;top:166px">Email <i>*</i></label>
      <div class="field" style="left:463px;top:185px;width:364px;height:24px"></div>
      <label style="left:463px;top:223px">Ihre Nachricht <i>*</i></label>
      <div class="field" style="left:463px;top:241px;width:607px;height:82px"></div>
    </div>
    <div class="abs send">Senden</div>
    <div class="legal">
      <a style="top:408px">Impressum</a>
      <a style="top:445px">Datenschutz</a>
      <a style="top:483px">AGB</a>
      <a style="top:521px">Liefer- und Zahlungsbedingungen</a>
    </div>
  </footer>
  <div class="abs bottom">Home/Geschichten/Über uns/Kontakt<br>Copyright Lunvo 2021</div>

</div>
</body>
</html>
```